Business Cards and email stationery for VoiceOver Artist
Cutting Edge Business cards and email stationery for VoiceOver Artist
Use standard fonts
Not sure here?
Bright & Fun-filled
Marcus Dellow
Voiceover
2817 Palmera Ave
Encino CA 91427
(•••NO ADDRESS ON BUSINESS CARDS PLEASE••••)
818-555-2193 Cell
marcus@marcusdellow.example
marcusdellow.example
As 3-D as possible, cutting-edge, creative
1 Should be easy to read
2 Cell number should be listed first!
Uploaded Logo for VoiceOver Artist for Business cards and email Stationery
Logo for VoiceOver Artist v2

```html
<!DOCTYPE html>
<html lang="en">
<head>
<meta charset="utf-8">
<title>Marcus Dellow – Voiceover Business Card</title>
<link rel="stylesheet" href="https://fonts.googleapis.com/css2?family=Michroma&family=Montserrat:wght@300;400;600&display=swap">
<style>
  :root {
    --bg: #e4e6ea;
    --red-light: #e5262c;
    --red: #c4121a;
    --red-dark: #7d0a10;
    --charcoal: #3a3a3c;
    --charcoal-dark: #232325;
    --silver: #d9dadc;
    --white: #ffffff;
    --muted: #c9c9cc;
  }
  * { margin: 0; padding: 0; box-sizing: border-box; }
  html, body { width: 1200px; height: 977px; overflow: hidden; }
  body {
    background: var(--bg);
    font-family: "Montserrat", Arial, sans-serif;
    display: flex;
    flex-direction: column;
    align-items: center;
    justify-content: center;
    gap: 40px;
  }
  .card {
    position: relative;
    width: 760px;
    height: 434px;
    border-radius: 26px;
    overflow: hidden;
    background: radial-gradient(ellipse at 60% 20%, var(--red-light) 0%, var(--red) 45%, var(--red-dark) 100%);
    box-shadow: 0 10px 30px rgba(0,0,0,.25);
  }
  .card-art { position: absolute; inset: 0; width: 100%; height: 100%; }

  /* front */
  .brand {
    position: absolute; left: 44px; top: 44px;
    display: flex; align-items: center; gap: 18px;
  }
  .brand-dot {
    width: 74px; height: 74px; border-radius: 50%;
    background: var(--silver);
    flex: none;
  }
  .brand-text { display: flex; flex-direction: column; gap: 6px; }
  .brand-name {
    font-family: "Michroma", Arial, sans-serif;
    font-size: 38px; color: var(--white); letter-spacing: 1px; line-height: 1;
  }
  .brand-role {
    font-family: "Michroma", Arial, sans-serif;
    font-size: 13px; color: var(--silver); letter-spacing: 14px;
  }
  .holder {
    position: absolute; left: 48px; top: 168px;
    color: var(--muted); text-transform: uppercase;
  }
  .holder-name { font-size: 15px; font-weight: 300; letter-spacing: 3px; }
  .holder-role { font-size: 11px; font-weight: 600; letter-spacing: 2px; margin-top: 6px; color: var(--silver); }

  .contact {
    position: absolute; right: 44px; bottom: 34px;
    list-style: none; color: var(--white);
    font-size: 14px; line-height: 1.75; letter-spacing: .5px;
  }
  .contact li { display: flex; align-items: center; gap: 9px; }
  .contact svg { width: 14px; height: 14px; flex: none; }

  /* back */
  .site-url {
    position: absolute; left: 48px; top: 40px;
    font-family: "Michroma", Arial, sans-serif;
    font-size: 16px; letter-spacing: 6px; color: var(--muted);
  }
</style>
</head>
<body>

  <section class="card card-front" aria-label="Business card front">
    <svg class="card-art" viewBox="0 0 760 434" preserveAspectRatio="none" aria-hidden="true">
      <defs>
        <linearGradient id="swoosh-grey" x1="0" y1="0" x2="0" y2="1">
          <stop offset="0" stop-color="#46464a"/>
          <stop offset="1" stop-color="#232325"/>
        </linearGradient>
        <linearGradient id="swoosh-silver" x1="0" y1="0" x2="1" y2="0">
          <stop offset="0" stop-color="#8e8f93"/>
          <stop offset=".5" stop-color="#f4f4f5"/>
          <stop offset="1" stop-color="#9a9b9f"/>
        </linearGradient>
      </defs>
      <path d="M0 218 C 150 226 290 280 380 360 C 405 384 420 410 430 434 L0 434 Z" fill="url(#swoosh-silver)"/>
      <path d="M0 232 C 150 242 280 296 366 372 C 388 394 402 414 410 434 L0 434 Z" fill="url(#swoosh-grey)"/>
    </svg>

    <div class="brand">
      <span class="brand-dot"></span>
      <div class="brand-text">
        <span class="brand-name">MARCUS DELLOW</span>
        <span class="brand-role">VOICEOVER</span>
      </div>
    </div>

    <div class="holder">
      <p class="holder-name">Marcus Dellow</p>
      <p class="holder-role">Voiceover</p>
    </div>

    <ul class="contact">
      <li>
        <svg viewBox="0 0 16 16"><circle cx="8" cy="8" r="8" fill="#fff"/><path d="M5.2 4h1.6l.8 2-1 .8a5 5 0 0 0 2.6 2.6l.8-1 2 .8v1.6c0 .5-.4.8-.9.8A7 7 0 0 1 4.4 4.9c0-.5.3-.9.8-.9z" fill="#c4121a"/></svg>
        818-555-2193 Cell
      </li>
      <li>
        <svg viewBox="0 0 16 16"><circle cx="8" cy="8" r="8" fill="#fff"/><rect x="4" y="5" width="8" height="6" rx="1" fill="#c4121a"/><path d="M4 5.5l4 3 4-3" stroke="#fff" fill="none" stroke-width=".9"/></svg>
        marcus@marcusdellow.example
      </li>
      <li>
        <svg viewBox="0 0 16 16"><circle cx="8" cy="8" r="8" fill="#fff"/><circle cx="8" cy="8" r="4.2" fill="none" stroke="#c4121a" stroke-width="1"/><path d="M3.8 8h8.4M8 3.8c-2 2.5-2 5.9 0 8.4M8 3.8c2 2.5 2 5.9 0 8.4" stroke="#c4121a" fill="none" stroke-width=".8"/></svg>
        www.marcusdellow.example
      </li>
    </ul>
  </section>

  <section class="card card-back" aria-label="Business card back">
    <svg class="card-art" viewBox="0 0 760 434" aria-hidden="true">
      <circle cx="560" cy="250" r="150" fill="none" stroke="#ffffff" stroke-opacity=".12" stroke-width="6"/>
    </svg>
    <p class="site-url">WWW.MARCUSDELLOW.EXAMPLE</p>
  </section>

</body>
</html>
```